German Headhunter/ HR Consultancy needs Business Cards Design

We need a business Card Design for our Company in Stuttgart. We are specialized as Headhunter/ HR Consultancy in Placement of specialist and managers in permanent employment. Please refer to our business logo.

```html
<!DOCTYPE html>
<html lang="en">
<head>
<meta charset="utf-8">
<title>Kernwerk Personalberatung – Business Card</title>
<link href="https://fonts.googleapis.com/css2?family=Karla:wght@400;500;700&display=swap" rel="stylesheet">
<style>
  :root {
    --page-bg: #e9e7e3;
    --card-light: #e4e1dc;
    --card-mid: #cfcac3;
    --card-dark: #8e8c8a;
    --navy: #1f2a78;
    --ink: #2a2b3a;
    --grey: #555659;
    --bar: #6e6e70;
  }
  * { margin: 0; padding: 0; box-sizing: border-box; }
  html, body { width: 1200px; height: 969px; overflow: hidden; }
  body {
    background: var(--page-bg);
    font-family: "Karla", Arial, sans-serif;
    position: relative;
  }
  .card {
    position: absolute;
    left: 50px; top: 172px;
    width: 1100px; height: 624px;
    border-radius: 28px;
    overflow: hidden;
    background: linear-gradient(100deg, var(--card-dark) 0%, var(--card-mid) 38%, var(--card-light) 70%, var(--card-mid) 100%);
    box-shadow: 0 8px 30px rgba(0,0,0,0.18);
  }
  .brand-mark {
    position: absolute;
    left: 92px; top: 156px;
    width: 330px; height: 330px;
    background: var(--navy);
    transform: rotate(45deg);
  }
  .brand-name {
    position: absolute;
    right: 61px; top: 80px;
    text-align: right;
    color: var(--navy);
    font-weight: 700;
    line-height: 1;
  }
  .brand-name .line-main { display: block; font-size: 66px; letter-spacing: 2px; }
  .brand-name .line-sub { display: block; font-size: 39px; margin-top: 6px; letter-spacing: 0.5px; }
  .accent-bar {
    position: absolute;
    left: 1089px; top: 229px;
    width: 9px; height: 63px;
    background: var(--bar);
  }
  .person {
    position: absolute;
    right: 61px; top: 234px;
    text-align: right;
  }
  .person-name {
    color: var(--navy);
    font-weight: 700;
    font-size: 32px;
    letter-spacing: 1px;
    line-height: 1;
  }
  .person-title {
    color: var(--grey);
    font-size: 22px;
    margin-top: 8px;
    letter-spacing: 0.5px;
    line-height: 1;
  }
  .contact-row {
    position: absolute;
    right: 62px;
    display: flex;
    align-items: center;
    gap: 16px;
    font-size: 22px;
    color: var(--ink);
    letter-spacing: 0.4px;
    line-height: 1;
  }
  .contact-row .icon { width: 22px; height: 22px; fill: var(--navy); flex: none; }
  .contact-row .icon.blank { visibility: hidden; }
</style>
</head>
<body>
  <div class="card">
    <div class="brand-mark" role="img" aria-label="Kernwerk brand mark"></div>

    <div class="brand-name">
      <span class="line-main">KERNWERK</span>
      <span class="line-sub">PERSONALBERATUNG</span>
    </div>

    <div class="accent-bar"></div>

    <div class="person">
      <div class="person-name">JONAS ALBRECHT</div>
      <div class="person-title">Founder &amp; CEO</div>
    </div>

    <div class="contact-row" style="top:334px">
      <span>4120 Linden Avenue</span>
      <svg class="icon" viewBox="0 0 24 24"><path d="M12 2a7 7 0 0 0-7 7c0 5 7 13 7 13s7-8 7-13a7 7 0 0 0-7-7zm0 9.5A2.5 2.5 0 1 1 12 6.5a2.5 2.5 0 0 1 0 5z"/></svg>
    </div>
    <div class="contact-row" style="top:365px">
      <span>Harbor City, Oregon 51823</span>
      <svg class="icon blank" viewBox="0 0 24 24"></svg>
    </div>
    <div class="contact-row" style="top:402px">
      <span>555-214-7730</span>
      <svg class="icon" viewBox="0 0 24 24"><path d="M6.6 10.8a15 15 0 0 0 6.6 6.6l2.2-2.2a1 1 0 0 1 1-.25 11.4 11.4 0 0 0 3.6.57 1 1 0 0 1 1 1V20a1 1 0 0 1-1 1A17 17 0 0 1 3 4a1 1 0 0 1 1-1h3.5a1 1 0 0 1 1 1c0 1.25.2 2.45.57 3.57a1 1 0 0 1-.25 1z"/></svg>
    </div>
    <div class="contact-row" style="top:433px">
      <span>555-382-1946</span>
      <svg class="icon" viewBox="0 0 24 24"><path d="M7 1h10a2 2 0 0 1 2 2v18a2 2 0 0 1-2 2H7a2 2 0 0 1-2-2V3a2 2 0 0 1 2-2zm0 3v15h10V4z"/></svg>
    </div>
    <div class="contact-row" style="top:464px">
      <span>555-607-5812</span>
      <svg class="icon" viewBox="0 0 24 24"><path d="M7 3h10v5H7zM4 9h16a2 2 0 0 1 2 2v6h-4v4H6v-4H2v-6a2 2 0 0 1 2-2zm4 6v4h8v-4z"/></svg>
    </div>
    <div class="contact-row" style="top:495px">
      <span>jonas@kernwerk.com</span>
      <svg class="icon" viewBox="0 0 24 24"><path d="M2 5h20v14H2zm2 2v.5l8 5 8-5V7z"/></svg>
    </div>
    <div class="contact-row" style="top:526px">
      <span>www.kernwerk.com</span>
      <svg class="icon" viewBox="0 0 24 24"><path d="M12 2a10 10 0 1 0 0 20 10 10 0 0 0 0-20zm-1 17.9A8 8 0 0 1 4.2 10L9 14.8v1.2a2 2 0 0 0 2 2zm6.9-2.5A2 2 0 0 0 16 16h-1v-3a1 1 0 0 0-1-1H8v-2h2a1 1 0 0 0 1-1V7h2a2 2 0 0 0 2-2v-.4a8 8 0 0 1 2.9 12.8z"/></svg>
    </div>
  </div>
</body>
</html>
```